'Private English tutoring'

I need a flyer design to advertise private English tutoring. I am offering lessons to ethnic minority groups in my local area in south Belfast. The biggest ethnic minorities groups are Chinese, Polish and Indian and African. I can teach at any level, from beginner English to advanced. The tutoring will be either one on one or small groups of four students. I can teach adults and children but my preference would be to teach adults.

The flyer would need to be easily understood by people who have English as a second language.

I am also offering proof reading and editing services to students at local universities and colleges.

Target Market(s)

Adults of ethnic minorities who may not speak or read much English

Industry/Entity Type

Tutoring

Font styles to use
Serif

Requirements
Must have
• It needs to communicate that I am an accredited TEFL (Teaching English as a Foreign language) tutor with 2 years experience and that I tutor Beginners - Advanced students. It would also need to say that I offer proof reading and editing services. It would also need to communicate the cost of lessons are £15, but there are group rates for groups of 2-4 students. It would need to include my contact details which are as follows: contact Mona Hargrove BTh at 07812609354 or email monahargroveenglish@quillpost.com
Nice to have
• In terms of design I would like it to be warm and inviting and something which would convey an atmosphere of learning for non English speakers. Other than that I don't have any preferences.
Should not have
• Nothing which is going to be offensive to ethnic minorities.
• No pictures of people

```html
<!DOCTYPE html>
<html lang="en">
<head>
<meta charset="utf-8">
<title>Private English Tutoring – Mona Hargrove</title>
<link rel="stylesheet" href="https://fonts.googleapis.com/css2?family=Arvo:ital,wght@0,400;0,700;1,400&family=Lora:ital,wght@0,400;0,600;1,400;1,600&display=swap">
<style>
  :root {
    --teal: #6dc9b6;
    --coral: #e5404e;
    --yellow: #ffe04f;
    --white: #ffffff;
    --rule: #a4d9e4;
    --mint-text: #b2e6dc;
  }
  * { margin: 0; padding: 0; box-sizing: border-box; }
  html, body { width: 847px; height: 1200px; overflow: hidden; }
  body { background: var(--teal); position: relative; font-family: "Lora", Georgia, serif; }

  .flyer {
    position: absolute; left: 62px; top: 56px; width: 723px; height: 1084px;
    background: var(--coral); color: var(--white); text-align: center;
  }
  .rules { position: absolute; inset: 0; }
  .flyer > *:not(.rules) { position: absolute; left: 0; right: 0; }

  .headline {
    font-family: "Arvo", Georgia, serif; font-weight: 700; color: var(--yellow);
    font-size: 104px; line-height: 1; letter-spacing: 3px;
  }
  .headline--learn { top: 44px; }
  .headline--english { top: 226px; }
  .tagline {
    top: 166px; font-style: italic; font-size: 48px; line-height: 1.1;
  }

  .service-title {
    top: 370px; font-family: "Arvo", Georgia, serif; font-weight: 400; font-size: 20px;
    letter-spacing: 1px; line-height: 56px;
  }
  .price {
    top: 452px; font-family: "Arvo", Georgia, serif; font-size: 32px; line-height: 52px;
  }
  .price__word { font-family: "Lora", Georgia, serif; font-style: italic; font-size: 29px; }
  .price__amount, .price__unit { font-weight: 700; }

  .group-rates { top: 534px; }
  .group-rates__title {
    font-family: "Arvo", Georgia, serif; font-weight: 700; font-size: 28px; line-height: 1.2;
  }
  .group-rates__detail { font-style: italic; font-size: 24px; line-height: 1.2; }

  .levels {
    top: 664px; font-size: 23px; line-height: 40px;
    display: flex; justify-content: center; align-items: center; gap: 12px;
  }
  .levels__arrow { width: 46px; height: 16px; }

  .credentials {
    top: 732px; font-size: 21px; color: var(--mint-text); letter-spacing: 0.3px;
  }

  .contact { top: 822px; font-style: normal; }
  .contact__title {
    font-family: "Arvo", Georgia, serif; font-weight: 700; font-size: 34px;
    letter-spacing: 2px; color: var(--yellow); line-height: 1.2;
  }
  .contact__line {
    font-family: "Arvo", Georgia, serif; font-weight: 700; font-size: 20px;
    line-height: 34px; color: var(--yellow);
  }

  .extra-services {
    top: 1006px; font-style: italic; font-size: 25px; line-height: 50px;
    color: var(--yellow);
  }
  .extra-services strong { font-weight: 600; }
</style>
</head>
<body>
  <main class="flyer">
    <svg class="rules" width="723" height="1084" viewBox="0 0 723 1084" fill="none" stroke="var(--rule)" stroke-width="2">
      <rect x="156" y="370" width="411" height="56"/>
      <rect x="162" y="376" width="399" height="44"/>
      <path d="M0 398 H156 M567 398 H723"/>
      <path d="M0 392 H156 M567 392 H723 M0 404 H156 M567 404 H723" stroke-width="1"/>
      <path d="M0 478 H200 M190 470 L202 478 L190 486"/>
      <path d="M723 478 H523 M533 470 L521 478 L533 486"/>
      <path d="M0 484 H194 M723 484 H529" stroke-width="1"/>
      <path d="M0 624 H150 V604 H170 V526 H553 V604 H573 V624 H723"/>
      <path d="M0 630 H156 V610 H176 V532 H547 V610 H567 V630 H723" stroke-width="1"/>
      <path d="M0 652 H90 V712 H633 V652 H723"/>
      <path d="M0 658 H84 V718 H639 V658 H723" stroke-width="1"/>
      <path d="M0 744 H60 M663 744 H723" stroke-width="1"/>
      <rect x="38" y="1006" width="647" height="50"/>
      <rect x="44" y="1012" width="635" height="38" stroke-width="1"/>
    </svg>

    <h1 class="headline headline--learn">LEARN</h1>
    <p class="tagline">to speak &amp; write in</p>
    <p class="headline headline--english">ENGLISH</p>

    <h2 class="service-title">PRIVATE ENGLISH TUTORING</h2>

    <p class="price"><span class="price__amount">£15</span> <span class="price__word">per</span> <span class="price__unit">LESSON</span></p>

    <div class="group-rates">
      <p class="group-rates__title">GROUP RATES</p>
      <p class="group-rates__detail">for groups of 2-4</p>
    </div>

    <p class="levels">
      <span>tutoring beginners</span>
      <svg class="levels__arrow" viewBox="0 0 50 16" fill="none" stroke="var(--white)" stroke-width="2.5"><path d="M0 8 H46 M38 1 L47 8 L38 15"/></svg>
      <span>advanced students</span>
    </p>

    <p class="credentials">accredited TEFL tutor with 2 years experience</p>

    <address class="contact">
      <p class="contact__title">CONTACT</p>
      <p class="contact__line">Mona Hargrove BTh</p>
      <p class="contact__line">07812609354</p>
      <p class="contact__line">monahargroveenglish@quillpost.com</p>
    </address>

    <p class="extra-services">Mona also offers <strong>proof reading</strong> and <strong>editing</strong> services.</p>
  </main>
</body>
</html>
```